Stationary package for modern new church start
Stationary for Bright Harbor Ministries
Stationary package for modern new church start  - Religion and Spirituality
Creative Brief
Professional
Daniel Mercer
Pastor
Bright Harbor Ministries P.O. Box 67890 Atlanta, GA 30318 The following P.O. Box is a generate one until I obtain one tomorrow. I will provide you with the correct P.O. Box sometime tomorrow or on Friday.
pastormercer@bhmx.org
www.bhmx.org
Please provide me with a complete stationary package that includes: Business Cards Letterhead Pen and pencil Email Signature USB Envelope Folder Fax Option Thank you Card front & Back Compliment Slip CD and CD Cover
Please include the following on the back: The Logo our our Ministry and our email address

```html
<!DOCTYPE html>
<html lang="en">
<head>
<meta charset="utf-8">
<title>Bright Harbor Ministries – Business Card</title>
<link href="https://fonts.googleapis.com/css2?family=Open+Sans:wght@400;600;700&display=swap" rel="stylesheet">
<style>
  :root {
    --backdrop: #e9e9ec;
    --card-white: #ffffff;
    --brand-red: #d7141c;
    --brand-red-light: #ef3a3f;
    --accent-blue: #1f9ad6;
    --rule-grey: #c9ccd2;
    --ink-soft: #6a6f78;
    --on-red: #ffffff;
  }
  html, body {
    margin: 0;
    padding: 0;
    width: 1200px;
    height: 901px;
    overflow: hidden;
    background: var(--backdrop);
    font-family: "Open Sans", Arial, sans-serif;
  }
  .business-card {
    position: absolute;
    left: 150px;
    top: 193px;
    width: 900px;
    height: 514px;
    border-radius: 44px;
    overflow: hidden;
    box-shadow: 0 18px 40px rgba(0,0,0,0.18);
  }
  .card-shapes {
    position: absolute;
    inset: 0;
  }
  .brand-block {
    position: absolute;
    left: 60px;
    top: 232px;
    width: 330px;
    text-align: center;
  }
  .brand-mark-dot {
    display: block;
    width: 64px;
    height: 64px;
    margin: 0 auto 16px;
    border-radius: 50%;
    background: var(--brand-red);
  }
  .brand-name {
    margin: 0;
    font-size: 29px;
    font-weight: 700;
    line-height: 1.15;
    color: var(--brand-red);
  }
  .brand-tagline {
    margin: 6px 0 0;
    font-size: 12px;
    font-weight: 400;
    letter-spacing: 0.5px;
    color: var(--ink-soft);
  }
  .contact-block {
    position: absolute;
    right: 46px;
    top: 74px;
    width: 340px;
    text-align: right;
    color: var(--on-red);
  }
  .contact-name {
    margin: 0;
    font-size: 21px;
    font-weight: 600;
    letter-spacing: 1px;
  }
  .contact-title {
    margin: 2px 0 0;
    font-size: 14px;
    font-weight: 400;
  }
  .contact-address {
    margin: 36px 0 0;
    font-size: 14px;
    line-height: 1.45;
  }
  .contact-lines {
    list-style: none;
    margin: 34px 0 0;
    padding: 0;
    font-size: 14px;
  }
  .contact-lines li {
    display: flex;
    justify-content: flex-end;
    align-items: center;
    gap: 10px;
    margin-bottom: 12px;
  }
  .contact-icon {
    width: 16px;
    height: 16px;
    flex: none;
  }
</style>
</head>
<body>
  <div class="business-card">
    <svg class="card-shapes" width="900" height="514" viewBox="0 0 900 514" aria-hidden="true">
      <defs>
        <linearGradient id="red-panel-fill" x1="0" y1="0" x2="1" y2="1">
          <stop offset="0" stop-color="var(--brand-red-light)"/>
          <stop offset="1" stop-color="var(--brand-red)"/>
        </linearGradient>
      </defs>
      <rect class="card-base" width="900" height="514" fill="var(--card-white)"/>
      <path class="grey-sweep" d="M250,0 C430,30 560,150 575,514" fill="none" stroke="var(--rule-grey)" stroke-width="3"/>
      <path class="blue-sweep" d="M300,0 C460,26 580,130 602,270" fill="none" stroke="var(--accent-blue)" stroke-width="14" stroke-linecap="round"/>
      <path class="red-panel" d="M400,0 C540,40 640,200 610,514 L900,514 L900,0 Z" fill="url(#red-panel-fill)"/>
    </svg>

    <div class="brand-block">
      <span class="brand-mark-dot"></span>
      <p class="brand-name">Bright Harbor Ministries</p>
      <p class="brand-tagline">Sharing the hope of grace</p>
    </div>

    <div class="contact-block">
      <p class="contact-name">DANIEL MERCER</p>
      <p class="contact-title">Managing Director</p>
      <p class="contact-address">P.O. Box 67890<br>Atlanta, GA 30318</p>
      <ul class="contact-lines">
        <li>404 555 0172
          <svg class="contact-icon" viewBox="0 0 16 16"><rect x="4" y="1" width="8" height="14" rx="2" fill="none" stroke="#fff" stroke-width="1.5"/><circle cx="8" cy="12.5" r="0.9" fill="#fff"/></svg>
        </li>
        <li>404 555 0173
          <svg class="contact-icon" viewBox="0 0 16 16"><path d="M4 2 L6.5 2 L7.5 5 L6 6.3 C6.8 8 8 9.2 9.7 10 L11 8.5 L14 9.5 L14 12 C14 13 13 14 12 14 C6.5 13.5 2.5 9.5 2 4 C2 3 3 2 4 2 Z" fill="#fff"/></svg>
        </li>
        <li>404 555 0174
          <svg class="contact-icon" viewBox="0 0 16 16"><rect x="2" y="5" width="12" height="8" rx="1" fill="#fff"/><rect x="4" y="2" width="8" height="4" fill="#fff"/></svg>
        </li>
        <li>pastormercer@bhmx.org
          <svg class="contact-icon" viewBox="0 0 16 16"><rect x="1.5" y="3.5" width="13" height="9" rx="1" fill="none" stroke="#fff" stroke-width="1.4"/><path d="M2 4 L8 9 L14 4" fill="none" stroke="#fff" stroke-width="1.4"/></svg>
        </li>
        <li>www.bhmx.org
          <svg class="contact-icon" viewBox="0 0 16 16"><circle cx="8" cy="8" r="6.3" fill="none" stroke="#fff" stroke-width="1.4"/><ellipse cx="8" cy="8" rx="2.8" ry="6.3" fill="none" stroke="#fff" stroke-width="1.2"/><path d="M1.8 8 H14.2" stroke="#fff" stroke-width="1.2"/></svg>
        </li>
      </ul>
    </div>
  </div>
</body>
</html>
```